Marlowe Creative Works Business Card Design

We need a double-sided business card for our company Marlowe Creative Works. Our slogan is "Simple Online Solutions." We are looking for a techy, cutting-edge but simple card that looks modern and sleek. We have a black logo attached and would prefer a lighter background to make our logo stand out. We like nice accents to make it pop out and make our clients remember our card.

On the back side, we just want our logo, slogan and website. Again, something very simple. Make the logo big on the back.

```html
<!DOCTYPE html>
<html lang="en">
<head>
<meta charset="utf-8">
<title>Marlowe Creative Works – Business Card</title>
<link href="https://fonts.googleapis.com/css2?family=Oswald:wght@300;400;500&family=Roboto+Condensed:wght@400;700&display=swap" rel="stylesheet">
<style>
  :root {
    --page: #a9a9a9;
    --card-light: #efede6;
    --card-light-edge: #e2dfd6;
    --ink: #141212;
    --band: #2a2120;
    --paper-text: #f3f1ea;
  }
  * { margin: 0; padding: 0; box-sizing: border-box; }
  html, body { width: 1200px; height: 1000px; overflow: hidden; }
  body {
    background: var(--page);
    font-family: "Oswald", "Roboto Condensed", sans-serif;
    color: var(--ink);
    position: relative;
  }
  .card {
    position: absolute;
    left: 285px;
    width: 630px;
    height: 360px;
    background: linear-gradient(135deg, var(--card-light) 0%, var(--card-light-edge) 100%);
    overflow: hidden;
    box-shadow: 0 10px 30px rgba(0,0,0,0.18);
  }
  .card--front { top: 95px; }
  .card--back { top: 545px; }
  .card svg.shape { position: absolute; inset: 0; }

  .brand { position: absolute; display: flex; flex-direction: column; }
  .brand__name {
    font-weight: 400;
    letter-spacing: 0.02em;
    color: var(--ink);
    white-space: nowrap;
  }
  .brand__slogan {
    font-family: "Roboto Condensed", sans-serif;
    font-weight: 700;
    text-transform: uppercase;
    letter-spacing: 0.22em;
    color: var(--ink);
  }

  /* Front */
  .card--front .brand { left: 250px; top: 48px; }
  .card--front .brand__name { font-size: 34px; }
  .card--front .brand__slogan { font-size: 11px; margin-top: 2px; }
  .holder {
    position: absolute;
    left: 34px;
    bottom: 40px;
    color: var(--paper-text);
  }
  .holder__name { font-size: 30px; font-weight: 500; line-height: 1.1; }
  .holder__role {
    font-family: "Roboto Condensed", sans-serif;
    font-size: 11px;
    font-weight: 700;
    text-transform: uppercase;
    letter-spacing: 0.14em;
  }
  .contact {
    position: absolute;
    left: 400px;
    top: 200px;
    list-style: none;
    font-size: 19px;
    font-weight: 400;
  }
  .contact li { display: flex; align-items: center; gap: 10px; line-height: 1.35; }
  .contact svg { width: 13px; height: 13px; flex: none; }

  /* Back */
  .card--back .brand { left: 70px; top: 118px; }
  .card--back .brand__name { font-size: 46px; }
  .card--back .brand__slogan { font-size: 15px; margin-top: 4px; letter-spacing: 0.25em; }
  .website {
    font-family: "Roboto Condensed", sans-serif;
    font-size: 15px;
    letter-spacing: 2px;
    fill: var(--paper-text);
  }
</style>
</head>
<body>

  <section class="card card--front" aria-label="Business card front">
    <svg class="shape" width="630" height="360" viewBox="0 0 630 360" aria-hidden="true">
      <polygon points="0,140 230,140 330,360 0,360" fill="var(--ink)"/>
    </svg>
    <div class="brand">
      <span class="brand__name">Marlowe Creative Works</span>
      <span class="brand__slogan">Simple Online Solutions</span>
    </div>
    <div class="holder">
      <div class="holder__name">Evan Harlow</div>
      <div class="holder__role">Marketing Director</div>
    </div>
    <ul class="contact">
      <li>
        <svg viewBox="0 0 13 13" aria-hidden="true"><rect x="2" y="1" width="9" height="11" rx="1.5" fill="none" stroke="var(--ink)" stroke-width="1.5"/></svg>
        555010204
      </li>
      <li>
        <svg viewBox="0 0 13 13" aria-hidden="true"><rect x="1" y="3" width="11" height="8" fill="var(--ink)"/></svg>
        info@mcw.com
      </li>
    </ul>
  </section>

  <section class="card card--back" aria-label="Business card back">
    <svg class="shape" width="630" height="360" viewBox="0 0 630 360">
      <polygon points="630,40 630,360 330,360" fill="var(--band)"/>
      <text class="website" text-anchor="middle" dominant-baseline="middle"
            transform="translate(500,228) rotate(-46.8)">www.marlowecreativeworks.com</text>
    </svg>
    <div class="brand">
      <span class="brand__name">Marlowe Creative Works</span>
      <span class="brand__slogan">Simple Online Solutions</span>
    </div>
  </section>

</body>
</html>
```